Brenfield Chiropractic Business Cards

[Front]
[KLV/Stormrider LOGO & Brenfield Chiropractic LOGO]
Neck & Back Pain Relief
Dr. Martin Pavely
Doctor of Chiropractic

• Short Term Care For Your Neck & Back Pain
• No Referral Needed
• Affordable / Insurance Accepted
• Proficient in treating Soft Tissue Problems

[Back]
For Valuable Wellness Letter Bulletins™ Emailed To You Free, Go To:
www.DrMartinPavelyJournal.example
[SpinaVault LOGO] - can be small

OFFICE HOURS:
Monday – Thursday
9 am - 12 noon, 2 pm - 6 pm
WALK-INS WELCOME

Industry/Entity Type

Business

Contact Information for Business Card

Brenfield Chiropractic Center, PLLC
4837 Tarrow Avenue, Suite K
Hollisford, NC 28999
(252) 555-0147
www.brenfieldchiro.example

Requirements
Must have
• The KLV/Stormrider Logo
The Brenfield Chiropractic Logo
Should not have
• A picture of a spine

```html
<!DOCTYPE html>
<html lang="en">
<head>
<meta charset="utf-8">
<title>Brenfield Chiropractic – Business Card Back</title>
<link href="https://fonts.googleapis.com/css2?family=Courgette&family=PT+Sans:wght@700&display=swap" rel="stylesheet">
<style>
  :root {
    --card-blue: #0553a3;
    --swoosh: #e4e6ea;
    --ink-light: #ffffff;
  }
  html, body {
    margin: 0;
    padding: 0;
    width: 1200px;
    height: 662px;
    overflow: hidden;
  }
  .card-back {
    position: relative;
    width: 1200px;
    height: 662px;
    background: var(--card-blue);
    overflow: hidden;
    color: var(--ink-light);
  }
  .swoosh {
    position: absolute;
    inset: 0;
    width: 1200px;
    height: 662px;
  }
  .swoosh path { fill: var(--swoosh); }
  .newsletter {
    position: absolute;
    left: 0;
    width: 1200px;
    top: 266px;
    text-align: center;
    font-family: "Courgette", cursive;
    margin: 0;
  }
  .newsletter-invite {
    font-size: 23px;
    margin: 0;
    line-height: 1;
  }
  .newsletter-url {
    font-size: 21px;
    margin: 18px 0 0;
    line-height: 1;
  }
  .partner-mark {
    display: inline-flex;
    align-items: center;
    gap: 8px;
    margin-top: 20px;
    font-family: "PT Sans", sans-serif;
    font-weight: 700;
    font-size: 29px;
    line-height: 1;
  }
  .partner-dot {
    width: 20px;
    height: 20px;
    border-radius: 50%;
    background: var(--ink-light);
  }
  .office-hours {
    position: absolute;
    left: 897px;
    top: 527px;
    font-family: "PT Sans", sans-serif;
    font-weight: 700;
  }
  .office-hours h2 {
    margin: 0 0 6px;
    font-size: 21px;
    line-height: 1;
  }
  .office-hours p {
    margin: 0;
    font-size: 16.5px;
    line-height: 22px;
  }
</style>
</head>
<body>
  <main class="card-back">
    <svg class="swoosh" viewBox="0 0 1200 662" aria-hidden="true">
      <path d="M0,404 C250,532 560,602 868,556 C560,590 250,548 0,421 Z"/>
      <path d="M1005,504 C1085,478 1150,440 1200,394 L1200,411 C1150,452 1085,486 1005,504 Z"/>
    </svg>

    <section class="newsletter">
      <p class="newsletter-invite">For Valuable Wellness Letter Bulletins™ Emailed To You Free, Go To:</p>
      <p class="newsletter-url">www.DrMartinPavelyJournal.example</p>
      <div class="partner-mark"><span class="partner-dot"></span>SpinaVault</div>
    </section>

    <section class="office-hours">
      <h2>OFFICE HOURS :</h2>
      <p>Monday – Thursday</p>
      <p>9 am - 12 noon, 2 pm - 6 pm</p>
      <p>WALK-INS WELCOME</p>
    </section>
  </main>
</body>
</html>
```